Backflow Prevention Test Gauge Calibration Service

Our company, Northfield Valve Supply Company, specializes in backflow prevention, a backflow preventer is a valve on the public drinking water system that prevents contamination. Backflow preventers need to be tested annually using a backflow test gauge. A backflow test gauge is considered an instrument and is required to be tested and calibrated annually to ensure they are working accurately. We offer that service, along with repair services if the instrument is damaged, and we refer to it as a "Hassle Free" service. We schedule the service for them once they provide their information and then email them a shipping label that they can print out, tape on their box and send the package from their business or home. We have a quick-turnaround time for this service because we understand how important this piece of equipment is for our customers to continue their job.

The main points we want to highlight on the flyer are:
* Hassle free shipping
* 1-Day turnaround time
* Service all gauge models
* Price includes incoming & return freight
* Honor all manufacturer warranties

We would like to include the manufacturers' logos and photos of the gauges that our customers use and will recognize (photos in brief).

There are two ways to schedule this service with us. They can call us at (800) 642-3871 or they can fill out a form on our website www.pipeguardshop.com.

Our text preferences are Myriad Pro and Tahoma. Our brand colors are red, white and blue. Please visit our website to get an idea of our style too.

```html
<!DOCTYPE html>
<html lang="en">
<head>
<meta charset="utf-8">
<title>Northfield Valve Supply Company – Test Gauge Calibration</title>
<link rel="stylesheet" href="https://fonts.googleapis.com/css2?family=Fira+Sans+Condensed:wght@400&family=Open+Sans:wght@400;700;800&display=swap">
<style>
  :root{
    --blue:#1d4f9c;
    --blue-dark:#123a7e;
    --blue-light:#2a62b4;
    --red:#d81f2a;
    --red-dark:#b5141e;
    --white:#ffffff;
    --strip:#e7e8ea;
    --page:#ececec;
    --ink:#1a1a1a;
  }
  *{margin:0;padding:0;box-sizing:border-box}
  html,body{width:1200px;height:1128px;overflow:hidden;background:var(--page)}
  body{font-family:"Open Sans",Tahoma,sans-serif}
  .flyer{position:absolute;left:174px;top:14px;width:852px;height:1100px;background:var(--white);overflow:hidden;box-shadow:0 2px 10px rgba(0,0,0,.15)}
  .hero-art{position:absolute;left:0;top:0;width:852px;height:540px}
  .brand{position:absolute;left:30px;top:38px;color:var(--blue)}
  .brand-name{font-size:32px;font-weight:400;line-height:1;display:flex;align-items:center;gap:12px}
  .brand-mark{width:18px;height:18px;background:var(--red);border-radius:50%}
  .brand-sub{font-size:16px;font-weight:400;margin-left:30px;margin-top:4px}
  .intro{position:absolute;left:37px;top:195px;color:var(--white)}
  .intro-lead{font-family:"Fira Sans Condensed",Tahoma,sans-serif;font-size:21px;margin-bottom:14px}
  .intro-list{list-style:none;font-size:31px;font-weight:700;line-height:43px;letter-spacing:.3px}
  .features{position:absolute;left:36px;top:536px;list-style:none}
  .feature{display:flex;align-items:center;height:66px;margin-bottom:11px}
  .feature-icon{width:68px;height:68px;flex:none}
  .feature-text{margin-left:12px;color:var(--blue);font-size:24px;font-weight:700;line-height:26px;width:300px}
  .gauge{position:absolute;border-radius:6px}
  .gauge-a{left:441px;top:576px;width:191px;height:146px;background:linear-gradient(160deg,#3a3a3a,#161616)}
  .gauge-b{left:660px;top:561px;width:139px;height:169px;background:linear-gradient(160deg,#d9d7cf,#b9b49d)}
  .gauge-c{left:441px;top:758px;width:195px;height:146px;background:linear-gradient(160deg,#8c8c86,#5e5f5b)}
  .gauge-d{left:679px;top:733px;width:120px;height:171px;background:linear-gradient(160deg,#1f8e9a,#163a3f)}
  .makers{position:absolute;left:0;top:940px;width:852px;height:87px;background:var(--strip);display:flex;align-items:center;justify-content:space-around;padding:0 20px}
  .maker{font-size:24px;font-weight:800;color:var(--ink);text-align:center;line-height:1.05}
  .footer{position:absolute;left:0;top:1034px;width:852px;height:66px}
  .footer-bar{position:absolute;inset:0}
  .footer-call{position:absolute;left:38px;top:16px;color:var(--white);font-size:21px;font-weight:700;display:flex;align-items:center;gap:8px}
  .footer-web{position:absolute;left:470px;top:12px;color:var(--white);font-size:21px;font-weight:700}
</style>
</head>
<body>
<main class="flyer">
  <svg class="hero-art" viewBox="0 0 852 540" aria-hidden="false">
    <defs>
      <linearGradient id="panel" x1="0" y1="0" x2="1" y2="1">
        <stop offset="0" stop-color="#2a62b4"/>
        <stop offset="1" stop-color="#123a7e"/>
      </linearGradient>
      <linearGradient id="silver" x1="0" x2="1">
        <stop offset="0" stop-color="#f2f2f2"/>
        <stop offset=".5" stop-color="#a9abae"/>
        <stop offset="1" stop-color="#e0e0e0"/>
      </linearGradient>
      <radialGradient id="photo" cx=".55" cy=".5" r=".6">
        <stop offset="0" stop-color="#a8865a"/>
        <stop offset=".55" stop-color="#8a8782"/>
        <stop offset="1" stop-color="#6f6d6a"/>
      </radialGradient>
    </defs>
    <rect x="0" y="0" width="852" height="493" fill="url(#panel)"/>
    <rect x="0" y="493" width="852" height="14" fill="url(#silver)"/>
    <path d="M0 0 H852 V96 L440 96 Q230 178 0 110 Z" fill="var(--white)"/>
    <path d="M0 116 Q232 186 448 98" fill="none" stroke="var(--red)" stroke-width="8"/>
    <circle cx="674" cy="245" r="302" fill="var(--red)"/>
    <circle cx="674" cy="245" r="292" fill="var(--white)"/>
    <circle cx="674" cy="245" r="284" fill="url(#photo)" role="img" aria-label="Photo of a brass backflow preventer valve with repair parts and a wrench on concrete"/>
  </svg>

  <header class="brand">
    <div class="brand-name"><span class="brand-mark"></span>Northfield Valve</div>
    <div class="brand-sub">Supply Company</div>
  </header>

  <section class="intro">
    <p class="intro-lead">Your Complete Source For:</p>
    <ul class="intro-list">
      <li>BACKFLOW</li>
      <li>PREVENTER REPAIR</li>
      <li>PARTS ACCESSORIES</li>
      <li>ENCLOSURES TEST</li>
      <li>GAUGE CALIBRATION</li>
    </ul>
  </section>

  <ul class="features">
    <li class="feature">
      <svg class="feature-icon" viewBox="0 0 68 68"><circle cx="34" cy="34" r="33" fill="var(--red)"/><circle cx="34" cy="34" r="27" fill="none" stroke="#fff" stroke-width="2"/><g fill="none" stroke="#fff" stroke-width="2.4"><rect x="18" y="25" width="20" height="15"/><path d="M38 29h7l5 6v5H38z"/><circle cx="24" cy="42" r="3" fill="var(--red)"/><circle cx="44" cy="42" r="3" fill="var(--red)"/></g></svg>
      <span class="feature-text">Hassle free shipping</span>
    </li>
    <li class="feature">
      <svg class="feature-icon" viewBox="0 0 68 68"><circle cx="34" cy="34" r="33" fill="var(--red)"/><circle cx="34" cy="34" r="27" fill="none" stroke="#fff" stroke-width="2"/><circle cx="34" cy="34" r="15" fill="none" stroke="#fff" stroke-width="2.4"/><path d="M34 34V22A12 12 0 0 1 46 34Z" fill="#fff"/></svg>
      <span class="feature-text">1-Day turnaround time</span>
    </li>
    <li class="feature">
      <svg class="feature-icon" viewBox="0 0 68 68"><circle cx="34" cy="34" r="33" fill="var(--red)"/><circle cx="34" cy="34" r="27" fill="none" stroke="#fff" stroke-width="2"/><g fill="none" stroke="#fff" stroke-width="2.4"><circle cx="34" cy="27" r="7"/><circle cx="34" cy="27" r="2.5"/><path d="M19 42c6-3 10-1 14 1h8M19 48c8 3 16 2 28-6"/></g></svg>
      <span class="feature-text">Service all gauge models</span>
    </li>
    <li class="feature">
      <svg class="feature-icon" viewBox="0 0 68 68"><circle cx="34" cy="34" r="33" fill="var(--red)"/><circle cx="34" cy="34" r="27" fill="none" stroke="#fff" stroke-width="2"/><path d="M22 38 38 22h10v10L32 48Z" fill="none" stroke="#fff" stroke-width="2.4"/><circle cx="43" cy="27" r="2" fill="#fff"/><text x="33" y="40" fill="#fff" font-size="13" font-weight="700" text-anchor="middle" font-family="Open Sans, sans-serif">$</text></svg>
      <span class="feature-text">Price includes incoming &amp; return freight</span>
    </li>
    <li class="feature">
      <svg class="feature-icon" viewBox="0 0 68 68"><circle cx="34" cy="34" r="33" fill="var(--red)"/><circle cx="34" cy="34" r="27" fill="none" stroke="#fff" stroke-width="2"/><g fill="none" stroke="#fff" stroke-width="2.4"><circle cx="34" cy="31" r="11"/><path d="M29 31l4 4 6-7M27 40l-4 9 5-1 2 4 4-8 4 8 2-4 5 1-4-9"/></g></svg>
      <span class="feature-text">Honor all manufacturer warranties</span>
    </li>
  </ul>

  <div class="gauge gauge-a" role="img" aria-label="Photo of a differential test gauge kit in an open black case with hoses"></div>
  <div class="gauge gauge-b" role="img" aria-label="Photo of a compact test gauge with coloured hoses"></div>
  <div class="gauge gauge-c" role="img" aria-label="Photo of a test gauge kit with carrying box and hoses"></div>
  <div class="gauge gauge-d" role="img" aria-label="Photo of a hand-held digital test gauge"></div>

  <section class="makers" aria-label="Gauge manufacturers we service">
    <span class="maker">Hale Brandt</span>
    <span class="maker">KORRA</span>
    <span class="maker">Plainsway Instrument</span>
    <span class="maker">VALDEN</span>
  </section>

  <footer class="footer">
    <svg class="footer-bar" viewBox="0 0 852 66" preserveAspectRatio="none">
      <rect width="852" height="66" fill="var(--blue)"/>
      <path d="M400 0H852V50H425Z" fill="var(--white)"/>
      <path d="M404 0H852V46H427Z" fill="var(--red)"/>
    </svg>
    <p class="footer-call">CALL US AT
      <svg width="22" height="22" viewBox="0 0 24 24"><path d="M6 3l3 1 1 5-2 1c1 3 3 5 6 6l1-2 5 1 1 3-2 3C10 21 3 14 3 5Z" fill="none" stroke="#fff" stroke-width="1.8"/></svg>
      (800) 642-3871</p>
    <p class="footer-web">WWW.PIPEGUARDSHOP.COM</p>
  </footer>
</main>
</body>
</html>
```